New management consulting website

I need a 4-5 page website that I can manage in WordPress on Hostlane.example for a new management consulting company. The website is www.torvik-example.com and the company name is Torvik Group LLC. The attached spec has an example of a draft site, layout and actual copy and includes company and contact information. I have more high-res images I can send.

Must include instruction/assistance loading the site to my WordPress dashboard.

Target Market(s)

Any business, especially SAAS

Industry/Entity Type

Consultant

Coding

Coded - Design and coding required

Number of Pages Required

4 page

Font styles to use
Sans Serif

Colors
0456a4

Requirements
Must have
• Modern and stylish

```html
<!DOCTYPE html>
<html lang="en">
<head>
<meta charset="utf-8">
<title>Torvik Consulting</title>
<link href="https://fonts.googleapis.com/css2?family=Josefin+Sans:wght@400;600;700&family=Poppins:wght@300;400;500;600&display=swap" rel="stylesheet">
<style>
:root{
  --navy:#073d80;
  --ink:#1c1c1c;
  --text:#6b6b6b;
  --muted:#9a9a9a;
  --soft:#f7f7f7;
  --white:#ffffff;
  --dark:#333333;
  --darker:#2a2a2a;
}
*{box-sizing:border-box;margin:0;padding:0}
html,body{width:1200px;height:4870px;overflow:hidden}
body{font-family:"Poppins",sans-serif;color:var(--text);background:var(--white);position:relative}
.heading{font-family:"Josefin Sans",sans-serif;color:var(--ink)}
.eyebrow{font-size:13px;color:var(--navy)}
.btn{position:absolute;display:flex;align-items:center;justify-content:center;font-family:"Josefin Sans",sans-serif;font-weight:600;font-size:14px;letter-spacing:.3px}
.btn-solid{background:var(--navy);color:var(--white);box-shadow:0 6px 14px rgba(7,61,128,.25)}
.btn-line{border:1.5px solid var(--ink);color:var(--ink);background:transparent}
.photo{position:absolute}

/* hero */
.hero{position:absolute;left:0;top:0;width:1200px;height:578px}
.hero-glow{position:absolute;left:0;top:0;width:1200px;height:578px;background:radial-gradient(circle at 12% 20%,rgba(255,250,220,.9),rgba(255,240,200,0) 45%)}
.nav{position:absolute;left:185px;top:23px;width:830px;height:57px;background:var(--white);display:flex}
.nav-logo{width:132px;background:var(--navy);color:var(--white);display:flex;align-items:center;justify-content:center;font-family:"Josefin Sans",sans-serif;font-weight:700;font-size:20px;letter-spacing:1px}
.nav-links{flex:1;display:flex;align-items:center;gap:34px;padding-left:78px;font-size:11px;color:#555}
.nav-links .active{color:var(--navy);font-weight:600;border-bottom:2px solid var(--navy);padding-bottom:3px}
.nav-phone{width:143px;background:var(--navy);color:var(--white);padding:11px 0 0 20px;font-size:10px;line-height:1.4}
.nav-phone strong{display:block;font-size:14px;font-weight:500}
.hero h1{position:absolute;left:184px;top:182px;font-family:"Josefin Sans",sans-serif;font-weight:400;font-size:41px;color:var(--ink);line-height:1.3}
.hero h1 b{display:block;color:var(--navy);font-weight:700;font-size:46px}
.hero p{position:absolute;left:185px;top:310px;width:380px;font-size:14px;color:#2a2a2a;line-height:1.6}

/* about */
.dots{position:absolute;left:143px;top:935px;width:190px;height:190px;background-image:radial-gradient(circle,#c9c9c9 2px,transparent 2.5px);background-size:24px 37px}
.about-text{position:absolute;left:610px;top:660px;width:340px}
.about-text h2{font-size:30px;font-weight:600;line-height:1.25;margin:16px 0 30px}
.about-text p{font-size:13.5px;line-height:1.72;margin-bottom:20px}

/* services */
.services{position:absolute;left:0;top:1183px;width:1200px;height:1927px;background:var(--soft)}
.center{position:absolute;left:0;width:1200px;text-align:center}
.section-title{font-size:30px;font-weight:600}
.svc{position:absolute;width:392px}
.svc .num{font-family:"Josefin Sans",sans-serif;font-weight:700;font-size:22px;color:var(--navy)}
.svc h3{font-family:"Poppins",sans-serif;font-weight:500;font-size:21px;color:var(--ink);margin:20px 0 22px}
.svc p{font-size:14.5px;line-height:1.55}

/* team */
.team-blue{position:absolute;left:590px;top:3110px;width:610px;height:507px;background:var(--navy)}
.team-text{position:absolute;left:643px;top:3185px;width:320px;color:var(--white)}
.team-text h2{font-family:"Josefin Sans",sans-serif;font-weight:600;font-size:32px;line-height:1.25;margin:20px 0 18px}
.team-text h4{font-size:19px;font-weight:500}
.team-text .role{font-size:11px;margin:6px 0 22px}
.team-text p{font-size:11px;line-height:1.9}
.social{display:flex;gap:14px;margin-top:10px}
.social i{width:8px;height:8px;border-radius:50%;background:currentColor;display:block}

/* blog */
.card{position:absolute;top:3805px;width:262px;height:395px;background:var(--white);box-shadow:0 8px 24px rgba(0,0,0,.06)}
.card .pic{height:205px}
.card .body{padding:30px 26px 0}
.card h5{font-size:14px;font-weight:600;color:var(--ink);line-height:1.45}
.card p{font-size:11px;line-height:1.8;margin:14px 0 16px}
.card .more{font-size:11px;color:var(--ink);display:flex;align-items:center;gap:10px}

/* newsletter + footer */
.footer{position:absolute;left:0;top:4380px;width:1200px;height:490px;background:var(--dark);color:#e8e8e8}
.news-title{position:absolute;left:184px;top:82px;font-family:"Josefin Sans",sans-serif;font-weight:600;font-size:30px;line-height:1.35;color:var(--white)}
.news-form{position:absolute;left:591px;top:77px;width:425px;height:72px;background:var(--white);border-radius:36px;display:flex;align-items:center;padding:0 8px 0 40px}
.news-form span{flex:1;font-size:11px;color:var(--muted);margin-left:16px}
.news-form b{width:118px;height:48px;border-radius:24px;background:var(--navy);color:var(--white);font-weight:500;font-size:15px;display:flex;align-items:center;justify-content:center}
.foot-col{position:absolute;top:235px;font-size:11px;line-height:2.7}
.foot-col h6{font-size:14px;font-weight:600;color:var(--white);margin-bottom:8px;line-height:1.5}
.foot-logo{font-family:"Josefin Sans",sans-serif;font-weight:700;font-size:21px;color:var(--white);letter-spacing:1px}
.contact-row{display:flex;gap:18px;align-items:flex-start;line-height:1.6;margin-bottom:18px}
.bottom{position:absolute;left:0;top:460px;width:1200px;height:30px;background:var(--darker);font-size:10.5px;display:flex;align-items:center;justify-content:space-between;padding:0 184px}
</style>
</head>
<body>

<header class="hero">
  <div class="photo" role="img" aria-label="Photo of two hikers celebrating with raised arms on a mountain ridge at sunrise" style="inset:0;background:linear-gradient(180deg,#f2d9a4 0%,#e3b877 30%,#b38b5f 55%,#5d5a5d 75%,#2f2c30 100%)"></div>
  <div class="hero-glow"></div>
  <nav class="nav">
    <div class="nav-logo">TORVIK</div>
    <div class="nav-links">
      <span class="active">Home</span><span>About Us</span><span>Service</span><span>Team</span><span>News</span><span>Contact us</span>
    </div>
    <div class="nav-phone">Available 24/7 -<strong>555-014-0200</strong></div>
  </nav>
  <h1>We are Professional<b>Business Consultants</b></h1>
  <p>Lorem ipsum dolor sit amet consectetur adipis incididunt ut labore et dolore magna.</p>
  <div class="btn btn-solid" style="left:185px;top:390px;width:134px;height:45px">Contact Us</div>
  <div class="btn btn-line" style="left:341px;top:390px;width:134px;height:45px;border-color:#3a3024">Our service</div>
</header>

<section class="about">
  <div class="dots"></div>
  <div class="photo" role="img" aria-label="Photo of people walking on a beach at sunset" style="left:184px;top:658px;width:332px;height:412px;background:linear-gradient(180deg,#7b7f86 0%,#c7a36a 40%,#9b6f3f 70%,#5a4a38 100%)"></div>
  <div class="photo" role="img" aria-label="Photo of a climber silhouetted on a rocky peak above misty hills" style="left:305px;top:810px;width:263px;height:290px;background:linear-gradient(160deg,#cfd8e2 0%,#98a8bb 45%,#2a2d33 70%,#111 100%);border:4px solid var(--white)"></div>
  <div class="about-text">
    <div class="eyebrow">About Us</div>
    <h2 class="heading">Amazing Things For<br>Your Business Consulting</h2>
    <p>The word 'Torvik' originates from old Northumbrian English language and means 'above, beyond'.</p>
    <p>At Torvik Consulting our approach is to help you rise above your day-to-day business challenges, and build unique, innovative solutions to move beyond them.</p>
  </div>
  <div class="btn btn-solid" style="left:610px;top:1013px;width:143px;height:53px">Learn More</div>
</section>

<section class="services">
  <div class="center eyebrow" style="top:85px">Our Service</div>
  <div class="center heading section-title" style="top:118px">Above And Beyond</div>

  <div class="svc" style="left:184px;top:222px">
    <div class="num">01</div>
    <h3>strategy &amp; Operations</h3>
    <p>Lorem Ipsum is simply dummy text of the printing and typesetting industry. Lorem Ipsum has been the industry's standard dummy text ever since the 1500s, when an unknown printer took a galley of type and scrambled it to make a type specimen book. It has survived not only five centuries, but also the leap into electronic typesetting, remaining essentially unchanged.was popularised in the 1960s with the release of Presstype sheets containing Lorem Ipsum passages.</p>
  </div>
  <div class="btn btn-line" style="left:187px;top:580px;width:143px;height:54px">Contact Us</div>
  <div class="photo" role="img" aria-label="Photo of two businessmen looking at a phone in a bright office" style="left:614px;top:227px;width:399px;height:442px;background:linear-gradient(180deg,#dfe3e6 0%,#b9c0c6 50%,#e8e8e8 100%);border:3px solid var(--white)"></div>

  <div class="photo" role="img" aria-label="Photo of a hand holding a smartphone showing charts beside a desktop computer" style="left:186px;top:737px;width:400px;height:440px;background:linear-gradient(135deg,#e6e8ea 0%,#c9cdd2 45%,#3a3d44 70%,#d8d0c6 100%);border:3px solid var(--white)"></div>
  <div class="svc" style="left:611px;top:745px">
    <div class="num">02</div>
    <h3>Data Analysis &amp; Insights</h3>
    <p>Lorem Ipsum is simply dummy text of the printing and typesetting industry. Lorem Ipsum has been the industry's standard dummy text ever since the 1500s, when an unknown printer took a galley of type and scrambled it to make a type specimen book. It has survived not only five centuries, but also the leap into electronic typesetting, remaining essentially unchanged.was popularised in the 1960s with the release of Presstype sheets containing Lorem Ipsum passages.</p>
  </div>
  <div class="btn btn-line" style="left:612px;top:1099px;width:143px;height:54px">Contact Us</div>

  <div class="svc" style="left:184px;top:1238px">
    <div class="num">03</div>
    <h3>Leadership Development</h3>
    <p>Lorem Ipsum is simply dummy text of the printing and typesetting industry. Lorem Ipsum has been the industry's standard dummy text ever since the 1500s, when an unknown printer took a galley of type and scrambled it to make a type specimen book. It has survived not only five centuries, but also the leap into electronic typesetting, remaining essentially unchanged.was popularised in the 1960s with the release of Presstype sheets containing Lorem Ipsum passages.</p>
  </div>
  <div class="btn btn-line" style="left:185px;top:1595px;width:143px;height:54px">Contact Us</div>
  <div class="photo" role="img" aria-label="Photo of a team working on laptops around a wooden table" style="left:614px;top:1247px;width:398px;height:440px;background:linear-gradient(160deg,#8c7a66 0%,#5b4c3f 45%,#2e2a28 75%,#6d5a48 100%)"></div>

  <div class="btn btn-solid" style="left:499px;top:1769px;width:200px;height:75px;font-size:20px">View More!</div>
</section>

<section class="team">
  <div class="photo" role="img" aria-label="Portrait photo of the founder in a light blue shirt in a bright office" style="left:0;top:3110px;width:590px;height:507px;background:linear-gradient(90deg,#e9eef4 0%,#f6f8fb 40%,#c6d4e6 60%,#f4f6f8 100%)"></div>
  <div class="team-blue"></div>
  <div class="team-text">
    <div style="font-size:13px">Our Team</div>
    <h2>Meet Our<br>Professional Team</h2>
    <h4>Daniel Hart</h4>
    <div class="role">Founder and Senior Consultant</div>
    <p>Lorem ipsum dolor sit amet, consectetur adipisicing elit, sed do eiusmod tempor incididunt ut labore et dolore magna aliqua.enim ad minim veniam, quis nostrud exercitation ullamco laboris nisi.</p>
    <div style="font-size:10px;margin-top:22px">Follow Us On</div>
    <div class="social"><i></i><i></i><i></i><i></i></div>
  </div>
</section>

<section class="blog">
  <div class="center eyebrow" style="top:3697px">Our Blog</div>
  <div class="center heading section-title" style="top:3740px">The Origins Of 'Torvik'</div>

  <article class="card" style="left:184px">
    <div class="pic" role="img" aria-label="Photo of a path through a tall green forest" style="background:linear-gradient(180deg,#c9d3a0 0%,#5d6b33 40%,#2f3a1c 75%,#6b5430 100%)"></div>
    <div class="body"><h5>The industry's standard dummy text ever since.</h5><p>Lorem ipsum dolor sit amet, consectetur adipisicing elit, sed do eiusmod.</p><div class="more">Read More <svg width="20" height="10" viewBox="0 0 20 10"><path d="M0 5h18M14 1l4 4-4 4" stroke="#073d80" stroke-width="1.5" fill="none"/></svg></div></div>
  </article>
  <article class="card" style="left:469px">
    <div class="pic" role="img" aria-label="Photo of green valleys under a golden sunset sky" style="background:linear-gradient(180deg,#e8c079 0%,#9fa89a 35%,#4f6b3c 65%,#2c3d22 100%)"></div>
    <div class="body"><h5>It has survived not only five centuries,</h5><p>Lorem ipsum dolor sit amet, consectetur adipisicing elit, sed</p><div class="more">Read More <svg width="20" height="10" viewBox="0 0 20 10"><path d="M0 5h18M14 1l4 4-4 4" stroke="#073d80" stroke-width="1.5" fill="none"/></svg></div></div>
  </article>
  <article class="card" style="left:754px">
    <div class="pic" role="img" aria-label="Photo of a wooden lake house beneath rocky mountains" style="background:linear-gradient(180deg,#b9c3c9 0%,#7d8a8c 40%,#6b4a33 65%,#3d4c4e 100%)"></div>
    <div class="body"><h5>It was popularised in the 1960s with the release.</h5><p>Lorem ipsum dolor sit amet, consectetur adipisicing elit, sed</p><div class="more">Read More <svg width="20" height="10" viewBox="0 0 20 10"><path d="M0 5h18M14 1l4 4-4 4" stroke="#073d80" stroke-width="1.5" fill="none"/></svg></div></div>
  </article>

  <div class="btn btn-solid" style="left:527px;top:4247px;width:146px;height:53px">Add Item</div>
</section>

<footer class="footer">
  <div class="news-title">Get Update By Signup<br>Newsletter.</div>
  <div class="news-form">
    <svg width="16" height="12" viewBox="0 0 16 12"><rect width="16" height="12" rx="1" fill="#333"/><path d="M1 1l7 5 7-5" stroke="#fff" stroke-width="1.3" fill="none"/></svg>
    <span>Enter your email</span>
    <b>Subscribe</b>
  </div>

  <div class="foot-col" style="left:184px;width:200px">
    <div class="foot-logo">TORVIK</div>
    <div style="line-height:1.6;margin-top:42px">Lorem ipsum dolor sit amet, con sectetur adipisicing. elited do eiusmod.</div>
    <div class="social" style="margin-top:22px;color:#e8e8e8"><i></i><i></i><i></i><i></i></div>
  </div>
  <div class="foot-col" style="left:484px"><h6>Categories</h6>Home<br>About Us<br>Service<br>Team</div>
  <div class="foot-col" style="left:662px"><h6>Help</h6>News<br>Contact Us<br>Returns Policy<br>Terms</div>
  <div class="foot-col" style="left:802px;width:230px">
    <h6>Contact Us</h6>
    <div class="contact-row" style="margin-top:12px"><svg width="12" height="12" viewBox="0 0 24 24"><path d="M6.6 10.8a15 15 0 006.6 6.6l2.2-2.2a1 1 0 011-.25 11.4 11.4 0 003.6.6 1 1 0 011 1V20a1 1 0 01-1 1A17 17 0 013 4a1 1 0 011-1h3.5a1 1 0 011 1 11.4 11.4 0 00.6 3.6 1 1 0 01-.25 1z" fill="#fff"/></svg>555-014-0200</div>
    <div class="contact-row"><svg width="12" height="10" viewBox="0 0 16 12"><rect width="16" height="12" rx="1" fill="#fff"/><path d="M1 1l7 5 7-5" stroke="#333" stroke-width="1.3" fill="none"/></svg>info@torvik-example.com</div>
    <div class="contact-row"><svg width="10" height="13" viewBox="0 0 10 14"><path d="M5 0a5 5 0 015 5c0 4-5 9-5 9S0 9 0 5a5 5 0 015-5z" fill="#fff"/><circle cx="5" cy="5" r="1.8" fill="#333"/></svg>48 Harbor Lane #210,<br>Fairview, ST 00000</div>
  </div>

  <div class="bottom">
    <span>Copyright © 2021 torvik-example.com</span>
    <span>Site Terms &nbsp;|&nbsp; Privacy &nbsp;|&nbsp; Advertisement &nbsp;|&nbsp; Contact Us</span>
  </div>
</footer>

</body>
</html>
```